Lumeva Botanics Natural baby skin and hair care

We need a look and feel for a line of baby care products. A lotion, Wash and baby oil. We already have an existing line of products and are now venturing into baby care. We want a natural look with "love, softness and a touch of earth and Africa'

Industry/Entity Type

Retail

Font styles to use
Script

Colors
fbed22
f78f20
9bcb3c

Requirements
Must have
• Natural elements
Should not have
• Red, Black abstract shapes

```html
<!DOCTYPE html>
<html lang="en">
<head>
<meta charset="utf-8">
<title>Lumeva baby lotion label</title>
<link href="https://fonts.googleapis.com/css2?family=Tenor+Sans&family=Dancing+Script:wght@500&display=swap" rel="stylesheet">
<style>
  :root {
    --backdrop: #e6e6ea;
    --label: #ffffff;
    --ink: #433d38;
    --rose: #f0709a;
    --cap-light: #f47a9e;
    --cap-dark: #d94c7a;
    --sage: #cfcba6;
    --sketch-tone: #e9e3dc;
  }
  * { margin: 0; padding: 0; box-sizing: border-box; }
  html, body { width: 1200px; height: 1200px; overflow: hidden; }
  body {
    background: var(--backdrop);
    position: relative;
    font-family: "Tenor Sans", sans-serif;
    color: var(--ink);
  }
  .cap {
    position: absolute;
    left: 522px; top: 82px;
    width: 156px; height: 208px;
    border-radius: 10px 10px 6px 6px;
    background: linear-gradient(90deg, var(--cap-light) 0%, var(--cap-light) 45%, var(--cap-dark) 100%);
  }
  .label {
    position: absolute;
    left: 390px; top: 300px;
    width: 420px; height: 812px;
    background: var(--label);
    border-radius: 42px 42px 30px 30px;
  }
  .label > * { position: absolute; left: 0; width: 100%; text-align: center; }
  .brand-name {
    top: 104px;
    font-weight: 400; font-size: 52px; line-height: 1;
    letter-spacing: 10px; text-indent: 10px;
  }
  .product-name {
    top: 160px;
    font-family: "Dancing Script", cursive;
    font-size: 68px; line-height: 1; color: var(--rose);
  }
  .maker-frame {
    top: 256px; left: 117px; width: 186px; height: 186px;
    border: 2px solid var(--sage);
    outline: 1px solid var(--sage); outline-offset: -7px;
    display: flex; flex-direction: column; align-items: center; justify-content: flex-end;
    padding-bottom: 26px; gap: 4px;
  }
  .maker-name { font-size: 22px; letter-spacing: 4px; text-indent: 4px; line-height: 1.1; color: var(--ink); }
  .claims {
    top: 472px;
    font-size: 18px; letter-spacing: 3px; line-height: 24px;
  }
  .tagline {
    top: 522px;
    font-family: "Dancing Script", cursive;
    font-size: 28px; line-height: 1; color: var(--rose);
  }
  .volume { top: 645px; font-size: 14px; }
  .herb-border {
    top: 660px; left: 32px; width: 356px; height: 150px;
    background: linear-gradient(180deg, rgba(233,227,220,0) 0%, var(--sketch-tone) 100%);
    border-radius: 0 0 24px 24px;
  }
</style>
</head>
<body>
  <div class="cap"></div>
  <main class="label">
    <h1 class="brand-name">LUMEVA</h1>
    <p class="product-name">baby lotion</p>
    <div class="maker-frame">
      <span class="maker-name">LUMEVA</span>
      <span class="maker-name">BOTANICS</span>
    </div>
    <p class="claims">ALL NATURAL<br>SHEA BUTTER &amp; HONEY</p>
    <p class="tagline" style="top:562px">moisturising and soothing</p>
    <p class="volume">250ml/8oz.</p>
    <div class="herb-border" role="img" aria-label="Hand-drawn line sketches of wild herbs and leafy stems along the bottom of the label"></div>
  </main>
</body>
</html>
```